" Window Blinds and Shutters Business Card Design"

We require a business card design for a new windows blinds and shutters company based in Sydney.
The business name is 'Larkvale Blinds and Shutters'.
We supply and install homes and businesses with internal and external window furnishings and finishes. This includes varieties of window blinds and window shutters.

Benefits of Larkvale Blinds and Shutters :
Added security and privacy,
The ability to control the amount of sunlight,
Regulate internal temperature.

Blinds varieties:
Roller Blinds, Double Roller Blinds, Roman Blinds, Vertical Blinds, Aluminium venetians, Timber venetians and PVC Venetians.

Shutters varieties:
Plantation Shutters, Aluminium Louvre Shutters, Roller Shutters and Security Shutters .
Updates

Hi Designers,

Please have a look at my Business card design brief. I need your help to start my new business.

Thanks,

Dorian.

Reason: not 100% happy with the options available, close to 90% happy, need a little more refinement. Thank You & Good Luck

Target Market(s)

Home owners, business owners, shift workers , and new home builders.

Industry/Entity Type

Security

Contact Information for Business Card

Larkvale Blinds and Shutters,

Dorian Kettlewell mobile: 0487561904,
Priya Hensworth mobile: 0472846015,

email: dorian.kettlewell@mailgrove.net
web: larkvaleblindsandshutters.com.au

Colors
ffffff
9d9d9d
f78f20

Requirements
Must have
• ON FRONT OF CARD
I have attached a picture of logo and need a designer to design a font logo for Larkvale Blinds and Shutters similar, or open to suggestions.

FRONT OF CARD
Company message/:
"Safeguarding windows by design"

BACK OF CARD
'For a FREE measure & quote call Dorian - 0487561904"
Nice to have
• Elegant yet professional.

Soft colours appealing to both male & female clients.

Should not have

• Unprofessional fonts

```html
<!DOCTYPE html>
<html lang="en">
<head>
<meta charset="utf-8">
<title>Larkvale Blinds and Shutters – Business Card</title>
<link rel="stylesheet" href="https://fonts.googleapis.com/css2?family=Roboto+Condensed:wght@300;700&display=swap">
<style>
  :root {
    --frame-red: #b3202c;
    --badge-red: #c83c4a;
    --card-white: #f6f6f6;
    --ink: #111111;
    --icon-grey: #9d9d9d;
    --divider-red: #c83c4a;
    --backdrop: #e9e6e1;
  }
  * { box-sizing: border-box; margin: 0; padding: 0; }
  html, body { width: 1200px; height: 1000px; overflow: hidden; }
  body {
    position: relative;
    background: var(--backdrop);
    font-family: "Roboto Condensed", "Arial Narrow", sans-serif;
    color: var(--ink);
  }
  .card {
    position: absolute;
    left: 226px;
    width: 746px;
    height: 406px;
    background: var(--frame-red);
    padding: 15px;
  }
  .card--front { top: 68px; }
  .card--back { top: 521px; }
  .card__face {
    position: relative;
    width: 100%;
    height: 100%;
    background: var(--card-white);
    border-radius: 14px;
    overflow: hidden;
  }
  .brand-badge {
    position: absolute;
    background: var(--badge-red);
    border-radius: 6px;
    display: flex;
    align-items: center;
    color: #ffffff;
    font-weight: 700;
  }
  .brand-badge__name { line-height: 0.95; }
  .brand-badge__mark {
    border-radius: 50%;
    background: #ffffff;
    flex: none;
  }
  .brand-badge--small {
    left: 208px; top: 18px; width: 299px; height: 58px;
    padding: 0 14px 0 10px; justify-content: space-between;
    font-size: 22px;
  }
  .brand-badge--small .brand-badge__mark { width: 34px; height: 34px; }
  .brand-badge--large {
    left: 61px; top: 129px; width: 593px; height: 117px;
    padding: 0 30px 0 18px; justify-content: space-between;
    font-size: 44px;
  }
  .brand-badge--large .brand-badge__mark { width: 70px; height: 70px; }

  .contact-name {
    position: absolute; top: 112px;
    font-size: 33px; font-weight: 700; letter-spacing: 0.3px;
    white-space: nowrap;
  }
  .contact-name--left { right: 388px; }
  .contact-name--right { left: 382px; }
  .contact-phone {
    position: absolute; top: 154px;
    display: flex; align-items: center; gap: 4px;
    font-size: 32px; font-weight: 300; white-space: nowrap;
  }
  .contact-phone--left { right: 388px; }
  .contact-phone--right { left: 382px; }
  .contact-divider {
    position: absolute; left: 356px; top: 102px;
    width: 0; height: 96px;
    border-left: 3px dashed var(--divider-red);
  }
  .contact-line {
    position: absolute; left: 0; width: 100%;
    text-align: center; font-weight: 300; font-size: 27px; white-space: nowrap;
  }
  .contact-line--email { top: 255px; }
  .contact-line--web { top: 333px; font-size: 26px; }
  .contact-icon { position: absolute; left: 336px; }
  .contact-icon--email { top: 220px; }
  .contact-icon--web { top: 292px; }
</style>
</head>
<body>
  <section class="card card--front" aria-label="Card front">
    <div class="card__face">
      <div class="brand-badge brand-badge--small">
        <span class="brand-badge__name">Larkvale Blinds<br>And Shutters</span>
        <span class="brand-badge__mark"></span>
      </div>

      <p class="contact-name contact-name--left">DORIAN KETTLEWELL</p>
      <p class="contact-phone contact-phone--left">
        <svg width="20" height="32" viewBox="0 0 20 32" aria-hidden="true"><rect x="1" y="1" width="18" height="30" rx="2" fill="var(--icon-grey)"/><rect x="4" y="4" width="12" height="9" fill="#fff"/><g fill="#fff"><rect x="4" y="16" width="3" height="3"/><rect x="8.5" y="16" width="3" height="3"/><rect x="13" y="16" width="3" height="3"/><rect x="4" y="21" width="3" height="3"/><rect x="8.5" y="21" width="3" height="3"/><rect x="13" y="21" width="3" height="3"/><rect x="4" y="26" width="3" height="3"/><rect x="8.5" y="26" width="3" height="3"/><rect x="13" y="26" width="3" height="3"/></g></svg>
        0487561904
      </p>

      <span class="contact-divider"></span>

      <p class="contact-name contact-name--right">PRIYA HENSWORTH</p>
      <p class="contact-phone contact-phone--right">
        0472846015
        <svg width="20" height="32" viewBox="0 0 20 32" aria-hidden="true"><rect x="1" y="1" width="18" height="30" rx="2" fill="var(--icon-grey)"/><rect x="4" y="4" width="12" height="9" fill="#fff"/><g fill="#fff"><rect x="4" y="16" width="3" height="3"/><rect x="8.5" y="16" width="3" height="3"/><rect x="13" y="16" width="3" height="3"/><rect x="4" y="21" width="3" height="3"/><rect x="8.5" y="21" width="3" height="3"/><rect x="13" y="21" width="3" height="3"/><rect x="4" y="26" width="3" height="3"/><rect x="8.5" y="26" width="3" height="3"/><rect x="13" y="26" width="3" height="3"/></g></svg>
      </p>

      <svg class="contact-icon contact-icon--email" width="42" height="30" viewBox="0 0 42 30" aria-hidden="true"><rect x="0" y="0" width="42" height="30" fill="var(--badge-red)"/><polyline points="2,2 21,18 40,2" fill="none" stroke="#fff" stroke-width="2.5"/><line x1="2" y1="28" x2="16" y2="14" stroke="#fff" stroke-width="2"/><line x1="40" y1="28" x2="26" y2="14" stroke="#fff" stroke-width="2"/></svg>
      <p class="contact-line contact-line--email">dorian.kettlewell@mailgrove.net</p>

      <svg class="contact-icon contact-icon--web" width="42" height="36" viewBox="0 0 42 36" aria-hidden="true"><g fill="none" stroke="var(--badge-red)" stroke-width="3"><circle cx="21" cy="18" r="15.5"/><ellipse cx="21" cy="18" rx="7" ry="15.5"/><line x1="21" y1="2.5" x2="21" y2="33.5"/><line x1="5.5" y1="18" x2="36.5" y2="18"/><line x1="8" y1="10" x2="34" y2="10"/><line x1="8" y1="26" x2="34" y2="26"/></g></svg>
      <p class="contact-line contact-line--web">www.larkvaleblindsandshutters.com.au</p>
    </div>
  </section>

  <section class="card card--back" aria-label="Card back">
    <div class="card__face">
      <div class="brand-badge brand-badge--large">
        <span class="brand-badge__name">Larkvale Blinds<br>And Shutters</span>
        <span class="brand-badge__mark"></span>
      </div>
    </div>
  </section>
</body>
</html>
```